Floristry Business Card Design Project

I have a logo now and am looking to incorporate this into a business card. I would like a double sided business card. I would like one side to be decorative so that it blends well when included with floral arrangements and that can also be used as the front of a card and the other side will contain the business details. The font on the business details side should be clear although some decorative font would be ok. I have included the logo files for use in the business card design.

Feel free to break up the logo and use certain aspects of it in the design. Really looking for something that stands out and that is really creative.

Industry/Entity Type

Floral

Requirements
Should not have
• Nothing tacky or corny. The logo should be clearly read (perhaps a background colour).

```html
<!DOCTYPE html>
<html lang="en">
<head>
<meta charset="utf-8">
<title>Petal Hollow – Business Card</title>
<link href="https://fonts.googleapis.com/css2?family=Lato:wght@400;700;900&display=swap" rel="stylesheet">
<style>
  :root {
    --backdrop: #e9ebea;
    --card: #ffffff;
    --frame: #7cc4a0;
    --brand: #6fb48f;
    --brand-soft: #a7c27f;
    --wreath-green: #bfe0c9;
    --wreath-leaf: #d6e6b4;
    --wreath-coral: #f3c7b8;
    --name: #5fa884;
    --ink: #4a4d4c;
    --icon-bg: #7cc4a0;
    --icon-fg: #ffffff;
  }
  * { box-sizing: border-box; margin: 0; padding: 0; }
  html, body {
    width: 1200px;
    height: 900px;
    overflow: hidden;
    background: var(--backdrop);
    font-family: "Lato", Arial, sans-serif;
  }
  .sheet {
    position: relative;
    width: 1200px;
    height: 900px;
  }
  .card {
    position: absolute;
    left: 250px;
    width: 700px;
    height: 400px;
    background: var(--card);
    border-radius: 24px;
    box-shadow: 0 6px 18px rgba(0,0,0,0.12);
  }
  .card--front { top: 40px; }
  .card--back  { top: 460px; }
  .card__frame {
    position: absolute;
    inset: 14px;
    border: 5px solid var(--frame);
    border-radius: 14px;
  }

  /* brand mark: one plain circle holding the wreath tones, plus the name */
  .brand {
    position: absolute;
    left: 0;
    right: 0;
    display: flex;
    flex-direction: column;
    align-items: center;
  }
  .brand__wreath {
    border-radius: 50%;
    background:
      radial-gradient(circle,
        var(--card) 0 54%,
        var(--wreath-leaf) 60%,
        var(--wreath-green) 72%,
        var(--wreath-coral) 86%,
        rgba(255,255,255,0) 100%);
  }
  .brand__name {
    color: var(--brand-soft);
    font-weight: 400;
    text-transform: uppercase;
    letter-spacing: 0.34em;
    white-space: nowrap;
  }
  .card--front .brand { top: 48px; }
  .card--front .brand__wreath { width: 220px; height: 220px; }
  .card--front .brand__name { margin-top: 22px; font-size: 30px; }

  .card--back .brand { top: 40px; }
  .card--back .brand__wreath { width: 150px; height: 150px; }
  .card--back .brand__name { margin-top: 8px; font-size: 15px; }

  /* owner */
  .owner {
    position: absolute;
    right: 62px;
    top: 222px;
    text-align: right;
  }
  .owner__name {
    color: var(--name);
    font-weight: 900;
    font-size: 24px;
    letter-spacing: 0.01em;
  }
  .owner__role {
    color: var(--ink);
    font-weight: 700;
    font-size: 16px;
    margin-top: 2px;
  }

  /* contacts */
  .contacts {
    position: absolute;
    left: 58px;
    bottom: 46px;
    list-style: none;
  }
  .contacts__item {
    display: flex;
    align-items: center;
    gap: 12px;
    color: var(--ink);
    font-weight: 700;
    font-size: 18px;
    margin-top: 10px;
  }
  .contacts__icon {
    width: 30px;
    height: 30px;
    flex: none;
  }
</style>
</head>
<body>
<main class="sheet">

  <section class="card card--front" aria-label="Card front">
    <div class="card__frame"></div>
    <div class="brand">
      <div class="brand__wreath" role="img" aria-label="Floral wreath ornament in soft green, leaf and coral tones"></div>
      <div class="brand__name">Petal Hollow</div>
    </div>
  </section>

  <section class="card card--back" aria-label="Card back">
    <div class="card__frame"></div>
    <div class="brand">
      <div class="brand__wreath" role="img" aria-label="Floral wreath ornament in soft green, leaf and coral tones"></div>
      <div class="brand__name">Petal Hollow</div>
    </div>

    <div class="owner">
      <div class="owner__name">YOUR NAME</div>
      <div class="owner__role">Owner &amp; Florist</div>
    </div>

    <ul class="contacts">
      <li class="contacts__item">
        <svg class="contacts__icon" viewBox="0 0 30 30" aria-hidden="true">
          <circle cx="15" cy="15" r="15" fill="var(--icon-bg)"/>
          <path d="M10 8.5c1-.8 2-.6 2.5.3l1.2 2.3c.4.8.2 1.5-.5 2l-.8.6c.7 1.7 2 3 3.7 3.8l.6-.8c.5-.7 1.2-.9 2-.5l2.3 1.2c.9.5 1.1 1.5.3 2.5-1 1.2-2.6 1.6-4.2.9-3.6-1.5-6.2-4.1-7.7-7.7-.6-1.6-.4-3.4 .6-4.6z" fill="var(--icon-fg)"/>
        </svg>
        <span>877-555-0142</span>
      </li>
      <li class="contacts__item">
        <svg class="contacts__icon" viewBox="0 0 30 30" aria-hidden="true">
          <circle cx="15" cy="15" r="15" fill="var(--icon-bg)"/>
          <rect x="8" y="10" width="14" height="10" rx="1" fill="none" stroke="var(--icon-fg)" stroke-width="1.8"/>
          <polyline points="8.5,10.5 15,16 21.5,10.5" fill="none" stroke="var(--icon-fg)" stroke-width="1.8"/>
        </svg>
        <span>hello@petalhollow.com</span>
      </li>
      <li class="contacts__item">
        <svg class="contacts__icon" viewBox="0 0 30 30" aria-hidden="true">
          <circle cx="15" cy="15" r="15" fill="var(--icon-bg)"/>
          <g fill="none" stroke="var(--icon-fg)" stroke-width="2" transform="rotate(-45 15 15)">
            <rect x="7" y="12" width="9" height="6" rx="3"/>
            <rect x="14" y="12" width="9" height="6" rx="3"/>
          </g>
        </svg>
        <span>www.petalhollow.com</span>
      </li>
    </ul>
  </section>

</main>
</body>
</html>
```